Web Design For Calloway Pool Service

We are working with a company that wants a website for their pool service. Some sites to use for content/competitors and inspiration:
https://sacramento.brimwaterpools.example/builder/newbuild/repair/ppc
https://coralbaypoolcareandmore.example/
https://lumoxpoolservice.example/
https://www.halvorsenspoolresurfacing.example/pool-renovation-ga/
Thank you for taking the time to consider designing a website for us. We are web developers based in Stockton, CA, USA. Most of our projects go through the same process. Understanding this process may help you win a project with us. We custom-code all of our websites in-house. We don’t have any requirements as to what tools you use for your design, but we prefer Figma files. For any design that we label as four-stars, we send it to the client for review. The client picks the final design they want us to use. Once we complete this process, we will continue to show additional clients all the four-star sites and purchase them later. Your designs will have multiple chances to sell. For better chances of success, we ask that you follow these guidelines.
IMAGES:
If you use any images or icons in the design, we ask that you have a link to the asset so we can purchase the image/icon. Most of the designs we submit do not have the customer’s images on them unless they have some great images. Be creative; show us the feeling you are trying to portray with your image choices. Use any royalty-free site you choose. We subscribe to Adobe and mainly use their images, but we can purchase images outside of Adobe. PLEASE NOTE: we will not submit designs to clients with watermarks on the images.
FONTS:
We ask that you identify the fonts used in the design. This can be done in a message if you want. We typically use Google Fonts and Adobe Fonts.
CONTENT:
We're always open to different content and ideas. We often submit designs with stock images so the client can see our vision. We typically take pictures after the website launch to use their images with our vision. Lorem Ipsum is fine for paragraphs, but we ask that you write the headers in correct English. We want to be able to show the vision and identify the sections of the website.
INSPIRATION:
We typically add a couple of links in the brief of websites we like to help you get started in your design.
REVISIONS:
We do not often ask for revisions of the designs unless we see something in the design that may not appeal to the client. If there are slight changes that we want to make, we do that in the development process.
FEEDBACK:
We rarely give feedback on designs during the design process. We are working on many website projects and do not have the time to provide feedback. We usually respond if your request is well thought out and asks specific questions, but a note asking “feedback, please” usually goes unanswered.

```html
<!DOCTYPE html>
<html lang="en">
<head>
<meta charset="utf-8">
<title>Calloway Pool Service</title>
<link href="https://fonts.googleapis.com/css2?family=Open+Sans:wght@400;600;700&family=Tinos:wght@400;700&display=swap" rel="stylesheet">
<style>
:root{
  --navy:#1b3a6b;
  --navy-deep:#1d3c73;
  --blue:#2d9cf5;
  --lavender:#f1eff6;
  --lilac:#e4ddf0;
  --ink:#2a2f3a;
  --muted:#7a7f8c;
  --footer:#232c3a;
  --white:#ffffff;
}
*{margin:0;padding:0;box-sizing:border-box}
html,body{width:1200px;height:4521px;overflow:hidden}
body{position:relative;background:var(--white);font-family:"Open Sans",sans-serif;color:var(--ink)}
.abs{position:absolute}
.serif{font-family:"Tinos",serif;font-weight:400}

/* header */
.contact-chip{display:flex;align-items:center;gap:10px;top:20px;font-size:11px;line-height:14px;color:var(--muted)}
.contact-chip b{display:block;color:var(--ink);font-size:11px}
.chip-icon{width:26px;height:26px;border-radius:50%;background:var(--navy);display:flex;align-items:center;justify-content:center}
.header-rule{top:66px;height:1px;background:#d9dce3}
.brand{left:480px;width:240px;top:34px;text-align:center;font-family:"Tinos",serif;font-size:26px;color:var(--navy);letter-spacing:1px}
.nav-link{top:88px;font-size:11px;color:var(--muted)}
.btn-book{left:879px;top:12px;width:182px;height:39px;border-radius:20px;background:var(--navy);color:#fff;font-size:11px;font-weight:700;display:flex;align-items:center;justify-content:center}

/* hero */
.hero{left:0;top:121px;width:1200px;height:800px;background:linear-gradient(100deg,#2b2620 0%,#4a4034 40%,#6d5b48 60%,#2c3d4a 100%)}
.hero-kicker{left:82px;top:364px;color:#fff;font-size:20px;font-weight:600;letter-spacing:7px}
.hero-title{left:76px;top:410px;color:#fff;font-size:48px;font-weight:700}
.hero-rule{left:77px;top:492px;width:703px;height:2px;background:#fff}
.hero-text{left:82px;top:522px;width:640px;color:#fff;font-size:16px;line-height:28px}
.btn{position:absolute;height:39px;border-radius:20px;display:flex;align-items:center;justify-content:center;font-size:13px;font-weight:700}
.btn-learn{left:82px;top:611px;width:146px;background:var(--blue);color:#fff}
.btn-quote{left:239px;top:611px;width:180px;background:#fff;color:var(--navy)}

/* about */
.about-photo{left:86px;top:957px;width:464px;height:464px;border-radius:50%;background:linear-gradient(135deg,#8fb5c9,#9aa3a8 45%,#c2332e 70%,#6d747b)}
.eyebrow{color:var(--blue);font-family:"Tinos",serif;font-size:16px}
.about-title{left:621px;top:1010px;font-size:38px;line-height:52px;color:var(--navy)}
.about-quote{left:621px;top:1130px;width:470px;padding-left:14px;border-left:2px solid var(--navy);font-size:13px;line-height:24px;color:var(--muted)}
.about-text{left:621px;top:1210px;width:470px;font-size:13px;line-height:23.5px;color:var(--muted)}
.btn-contact{left:619px;top:1359px;width:155px;height:46px;background:var(--blue);color:#fff;font-size:15px;font-weight:600;display:flex;align-items:center;justify-content:center;gap:12px}

/* services */
.services{left:0;top:1512px;width:1200px;height:572px;background:var(--lavender)}
.section-title{left:0;width:1200px;text-align:center;color:var(--navy);font-size:46px}
.section-sub{left:0;width:1200px;text-align:center;color:var(--muted);font-size:13px;line-height:24px}
.service-card{top:1749px;width:320px;height:268px;border-radius:4px}
.service-card h3{position:absolute;left:20px;top:64px;font-family:"Tinos",serif;font-size:30px;font-weight:700;color:#fff}
.service-card svg.arrow{position:absolute;left:40px;top:212px}
.card-badge{width:70px;height:70px;border-radius:50%;background:#fff;box-shadow:0 4px 12px rgba(0,0,0,.12);display:flex;align-items:center;justify-content:center}

/* why choose */
.why-lobe{top:2319px;height:428px;border-radius:214px}
.why-photo{left:407px;top:2298px;width:386px;height:386px;border-radius:50%;background:linear-gradient(180deg,#e7e6ea,#9aa0aa 60%,#6f7682)}
.why-icon{width:84px;height:84px;border-radius:50%;background:var(--navy);border:4px solid #fff;box-shadow:0 0 0 2px #b8c3dd;display:flex;align-items:center;justify-content:center}
.why-item{width:260px}
.why-item h4{font-family:"Tinos",serif;font-weight:400;font-size:23px;color:var(--navy)}
.why-item p{margin-top:8px;font-size:12.5px;line-height:23px;color:var(--muted)}
.why-left{text-align:right;left:117px}
.why-right{text-align:left;left:796px}

/* appointment */
.appointment{left:0;top:2814px;width:1200px;height:562px;background:linear-gradient(120deg,#1c2a2f,#2e3d3a 45%,#24313a)}
.hours-title{left:93px;top:2946px;color:#fff;font-size:28px}
.hours-bar{left:94px;top:3010px;width:4px;height:235px;background:var(--blue)}
.hours-row{left:133px;width:420px;display:flex;justify-content:space-between;font-size:15px;color:#fff}
.hours-row span:first-child{font-weight:600}
.hours-row span:last-child{color:#cfd3da}
.form-panel{left:610px;top:2842px;width:492px;height:496px;background:var(--lilac)}
.form-icon{left:663px;top:2876px;width:58px;height:58px;border-radius:50%;background:var(--navy);display:flex;align-items:center;justify-content:center}
.field{height:52px;background:#fff;font-size:14px;color:var(--ink);display:flex;align-items:center;padding-left:28px}
.submit{left:665px;top:3264px;width:384px;height:53px;background:var(--blue);color:#fff;font-size:19px;font-weight:700;display:flex;align-items:center;justify-content:center}

/* reviews */
.reviews{left:0;top:3376px;width:1200px;height:620px;background:var(--lavender)}
.review-card{top:3652px;width:321px;height:265px;background:#fff;box-shadow:0 4px 18px rgba(30,40,80,.06);padding:58px 26px 0 26px}
.review-card.active{border-bottom:4px solid var(--navy)}
.stars{color:#f58a1f;font-size:15px;letter-spacing:3px}
.review-card p{margin-top:6px;font-size:12.5px;line-height:23px;color:var(--muted)}
.review-card h5{margin-top:10px;font-family:"Tinos",serif;font-weight:400;font-size:20px;color:var(--ink)}
.review-card small{display:block;margin-top:4px;font-size:9px;font-weight:700;color:#6d5bb5}
.avatar{top:3618px;width:60px;height:60px;border-radius:50%;background:linear-gradient(135deg,#d9c9b8,#8a7665);border:3px solid #fff}
.quote-mark{top:3620px;font-family:"Tinos",serif;font-size:110px;line-height:110px;color:#a9d4fb;font-weight:700}

/* footer */
.footer{left:0;top:3947px;width:1200px;height:502px;background:var(--footer)}
.footer-brand{left:400px;width:400px;top:4190px;text-align:center;font-family:"Tinos",serif;font-size:30px;color:#fff;letter-spacing:1px}
.footer-link{top:4280px;font-size:14px;color:#fff;transform:translateX(-50%)}
.footer-rule{left:333px;top:4332px;width:728px;height:1px;background:#4b5566}
.footer-divider{top:4368px;width:1px;height:70px;background:#4b5566}
.footer-contact{top:4376px;display:flex;align-items:center;gap:14px;color:#fff;font-size:12px;line-height:18px}
.footer-contact .ring{width:54px;height:54px;border-radius:50%;border:1px solid #9aa3b2;display:flex;align-items:center;justify-content:center}
.bottom-bar{left:0;top:4449px;width:1200px;height:72px;background:var(--navy-deep)}
.bottom-bar span{position:absolute;left:147px;top:26px;color:#fff;font-size:13px}
.social{top:4473px;width:24px;height:24px;border:1px solid #fff;background:transparent}
</style>
</head>
<body>

<!-- header -->
<div class="abs contact-chip" style="left:124px">
  <div class="chip-icon"><svg width="12" height="12" viewBox="0 0 24 24"><path fill="#fff" d="M6.6 10.8a15 15 0 0 0 6.6 6.6l2.2-2.2c.3-.3.7-.4 1-.2 1.1.4 2.3.6 3.6.6.6 0 1 .4 1 1V20c0 .6-.4 1-1 1A17 17 0 0 1 3 4c0-.6.4-1 1-1h3.5c.6 0 1 .4 1 1 0 1.3.2 2.5.6 3.6.1.3 0 .7-.2 1z"/></svg></div>
  <div><b>Call Us:</b>(209) 555-0148</div>
</div>
<div class="abs contact-chip" style="left:281px">
  <div class="chip-icon"><svg width="12" height="12" viewBox="0 0 24 24"><path fill="#fff" d="M3 5h18v14H3z"/><path fill="none" stroke="#1b3a6b" stroke-width="2" d="M3 5l9 7 9-7"/></svg></div>
  <div><b>Email:</b>office@callowaypools.example</div>
</div>
<div class="abs header-rule" style="left:122px;width:360px"></div>
<div class="abs header-rule" style="left:702px;width:360px"></div>
<div class="abs brand">Calloway Pool Service</div>
<div class="abs btn-book">BOOK APPOINTMENT</div>
<div class="abs nav-link" style="left:125px">Home</div>
<div class="abs nav-link" style="left:237px">About Us</div>
<div class="abs nav-link" style="left:386px">Services</div>
<div class="abs nav-link" style="left:705px">Team</div>
<div class="abs nav-link" style="left:831px">Blog</div>
<div class="abs nav-link" style="left:956px">Contact Us</div>

<!-- hero -->
<div class="abs hero" role="img" aria-label="Photo of a woman relaxing at the edge of a pool at sunset"></div>
<svg class="abs" style="left:0;top:700px" width="1200" height="240" viewBox="0 0 1200 240">
  <path d="M0,90 Q600,262 1200,90 L1200,240 L0,240Z" fill="#fff"/>
  <path d="M245,158 Q600,222 955,158" fill="none" stroke="#2d9cf5" stroke-width="4"/>
  <circle cx="600" cy="191" r="30" fill="#fff" stroke="#e3e6ee"/>
</svg>
<div class="abs hero-kicker">Crafting</div>
<div class="abs hero-title">Memories, One Pool at a Time</div>
<div class="abs hero-rule"></div>
<div class="abs hero-text">Lorem ipsum dolor sit amet, consectetur adipiscing elit, sed do eiusmod tempor incididunt ut labore et dolore magna</div>
<div class="btn btn-learn">LEARN MORE</div>
<div class="btn btn-quote">REQUEST QUOTE</div>

<!-- about -->
<svg class="abs" style="left:78px;top:952px" width="480" height="480" viewBox="0 0 480 480">
  <path d="M60,90 A232,232 0 1 1 160,455" fill="none" stroke="#1b3a6b" stroke-width="6"/>
</svg>
<div class="abs about-photo" role="img" aria-label="Photo of a technician servicing pool equipment with a toolbox"></div>
<div class="abs eyebrow" style="left:621px;top:976px">About Us</div>
<div class="abs about-title serif">Inspired Designs,<br>Impeccable Craftsmanship</div>
<div class="abs about-quote">Lorem ipsum dolor sit amet, consectetur adipiscing elit, sed do eiusmod or incididunt ut labore et dolore</div>
<div class="abs about-text">Lorem ipsum dolor sit amet, consectetur adipiscing elit, sed do eiusmod obgr incididunt ut labore et dolore Lorem ipsum dolor sit amet, consectetur adip iscing elit, sed do eiusmod tempor incididunt ut labore et dolore m agna aliqua. Ut enim ad minim veniam, quis nostrud exercitation ullamco laboris nisi ut aliquip ex ea commodo consequat.</div>
<div class="abs btn-contact">Contact us
  <svg width="18" height="12" viewBox="0 0 18 12"><path d="M0 6h16M11 1l5 5-5 5" fill="none" stroke="#fff" stroke-width="1.6"/></svg>
</div>

<!-- services -->
<div class="abs services"></div>
<div class="abs section-title serif" style="top:1560px">Our Services</div>
<div class="abs section-sub" style="top:1626px">Lorem ipsum dolor sit amet, consectetur adipiscing elit, sed do eiusmod temp<br>or incididunt ut labore et dolore</div>

<div class="abs service-card" style="left:91px;background:linear-gradient(160deg,#4f7993,#2b4a66 60%,#5d6f7c)" role="img" aria-label="Photo of a worker repairing pool tiles">
  <h3>Pool Repair</h3>
  <svg class="arrow" width="46" height="16" viewBox="0 0 46 16"><path d="M0 8h44M36 1l8 7-8 7" fill="none" stroke="#fff" stroke-width="1.5"/></svg>
</div>
<div class="abs service-card" style="left:438px;background:linear-gradient(160deg,#5d6670,#8a8c6d 55%,#3b4148)" role="img" aria-label="Photo of construction workers in hard hats on site">
  <h3>Pool Construction</h3>
  <svg class="arrow" width="46" height="16" viewBox="0 0 46 16"><path d="M0 8h44M36 1l8 7-8 7" fill="none" stroke="#fff" stroke-width="1.5"/></svg>
</div>
<div class="abs service-card" style="left:786px;background:linear-gradient(160deg,#8a9aa4,#3f9bbf 45%,#8a5a3c)" role="img" aria-label="Photo of a family enjoying a clean pool">
  <h3>Pool Cleaning</h3>
  <svg class="arrow" width="46" height="16" viewBox="0 0 46 16"><path d="M0 8h44M36 1l8 7-8 7" fill="none" stroke="#fff" stroke-width="1.5"/></svg>
</div>
<div class="abs card-badge" style="left:135px;top:1714px"><svg width="30" height="30" viewBox="0 0 24 24"><path d="M12 3l2.7 5.6 6.1.9-4.4 4.3 1 6.1L12 17l-5.4 2.9 1-6.1L3.2 9.5l6.1-.9z" fill="none" stroke="#2d9cf5" stroke-width="1.5"/></svg></div>
<div class="abs card-badge" style="left:482px;top:1714px"><svg width="30" height="30" viewBox="0 0 24 24"><circle cx="14" cy="5" r="2.2" fill="none" stroke="#2d9cf5" stroke-width="1.5"/><path d="M8 16l5-6 3 3M4 20h16M6 18c2-1 4 1 6 0s4 1 6 0" fill="none" stroke="#2d9cf5" stroke-width="1.5"/></svg></div>
<div class="abs card-badge" style="left:831px;top:1714px"><svg width="30" height="30" viewBox="0 0 24 24"><circle cx="8" cy="8" r="3" fill="none" stroke="#2d9cf5" stroke-width="1.5"/><circle cx="16" cy="8" r="3" fill="none" stroke="#2d9cf5" stroke-width="1.5"/><path d="M2 19c0-3 3-5 6-5s6 2 6 5M12 15c1-1 2.5-1 4-1 3 0 6 2 6 5" fill="none" stroke="#2d9cf5" stroke-width="1.5"/></svg></div>

<!-- why choose us -->
<div class="abs section-title serif" style="top:2136px">Why Choose Us</div>
<div class="abs section-sub" style="top:2203px">Lorem ipsum dolor sit amet, consectetur adipiscing elit, sed do eiusmod temp<br>or incididunt ut labore et dolore</div>
<div class="abs why-lobe" style="left:140px;width:500px;background:linear-gradient(90deg,rgba(241,239,246,0),#ebe6f3)"></div>
<div class="abs why-lobe" style="left:560px;width:500px;background:linear-gradient(270deg,rgba(241,239,246,0),#ebe6f3)"></div>
<div class="abs why-photo" role="img" aria-label="Photo of a smiling businessman with arms crossed"></div>

<div class="abs why-icon" style="left:398px;top:2361px"><svg width="30" height="30" viewBox="0 0 24 24"><path d="M5 17a8 8 0 1 1 14 0M12 13l3-4" fill="none" stroke="#fff" stroke-width="1.6"/></svg></div>
<div class="abs why-icon" style="left:398px;top:2493px"><svg width="30" height="30" viewBox="0 0 24 24"><path d="M12 3l2.7 5.6 6.1.9-4.4 4.3 1 6.1L12 17l-5.4 2.9 1-6.1L3.2 9.5l6.1-.9z" fill="none" stroke="#fff" stroke-width="1.6"/></svg></div>
<div class="abs why-icon" style="left:398px;top:2624px"><svg width="30" height="30" viewBox="0 0 24 24"><circle cx="14" cy="5" r="2.2" fill="none" stroke="#fff" stroke-width="1.6"/><path d="M8 16l5-6 3 3M4 20h16" fill="none" stroke="#fff" stroke-width="1.6"/></svg></div>
<div class="abs why-icon" style="left:693px;top:2361px"><svg width="30" height="30" viewBox="0 0 24 24"><circle cx="8" cy="8" r="3" fill="none" stroke="#fff" stroke-width="1.6"/><circle cx="16" cy="8" r="3" fill="none" stroke="#fff" stroke-width="1.6"/><path d="M2 19c0-3 3-5 6-5s6 2 6 5M12 15c1-1 2.5-1 4-1 3 0 6 2 6 5" fill="none" stroke="#fff" stroke-width="1.6"/></svg></div>
<div class="abs why-icon" style="left:693px;top:2493px"><svg width="30" height="30" viewBox="0 0 24 24"><circle cx="12" cy="13" r="8" fill="none" stroke="#fff" stroke-width="1.6"/><path d="M12 13l4-4" stroke="#fff" stroke-width="1.6"/></svg></div>
<div class="abs why-icon" style="left:693px;top:2624px"><svg width="30" height="30" viewBox="0 0 24 24"><path d="M19 8a8 8 0 0 0-14 2M5 16a8 8 0 0 0 14-2M19 3v5h-5M5 21v-5h5" fill="none" stroke="#fff" stroke-width="1.6"/></svg></div>

<div class="abs why-item why-left" style="top:2358px"><h4>Quality Assurance</h4><p>Lorem ipsum dolor sit amet, conser adi<br>or incididunt ut labore et dolore</p></div>
<div class="abs why-item why-left" style="top:2490px"><h4>Proven Record</h4><p>Lorem ipsum dolor sit amet, conser adi<br>or incididunt ut labore et dolore</p></div>
<div class="abs why-item why-left" style="top:2623px"><h4>Personalized Approach</h4><p>Lorem ipsum dolor sit amet, conser adi<br>or incididunt ut labore et dolore</p></div>
<div class="abs why-item why-right" style="top:2358px"><h4>Comprehensive Services</h4><p>Lorem ipsum dolor sit amet, conser adi<br>or incididunt ut labore et dolore</p></div>
<div class="abs why-item why-right" style="top:2490px"><h4>Professionalism</h4><p>Lorem ipsum dolor sit amet, conser adi<br>or incididunt ut labore et dolore</p></div>
<div class="abs why-item why-right" style="top:2623px"><h4>Experience and Expertise</h4><p>Lorem ipsum dolor sit amet, conser adi<br>or incididunt ut labore et dolore</p></div>

<!-- appointment -->
<div class="abs appointment" role="img" aria-label="Photo of a backyard pool at dusk with a dark overlay"></div>
<div class="abs hours-title serif">Opening Hours</div>
<div class="abs hours-bar"></div>
<div class="abs hours-row" style="top:3040px"><span>Monday - Thursday</span><span>08am - 05pm</span></div>
<div class="abs hours-row" style="top:3091px"><span>Saturday</span><span>08am - 02pm</span></div>
<div class="abs hours-row" style="top:3142px"><span>Phone</span><span>+123 456 7890</span></div>
<div class="abs hours-row" style="top:3193px"><span>Email</span><span>info@company.com</span></div>

<div class="abs form-panel"></div>
<div class="abs form-icon"><svg width="26" height="26" viewBox="0 0 24 24"><path d="M3 9l9-6 9 6v11H3z M3 9l9 6 9-6" fill="none" stroke="#fff" stroke-width="1.5"/></svg></div>
<div class="abs" style="left:733px;top:2876px;font-size:14px;color:var(--ink)">Get in touch with us any day any time</div>
<div class="abs serif" style="left:733px;top:2900px;font-size:35px;color:var(--ink)">Make Appointment</div>
<div class="abs field" style="left:665px;top:2975px;width:182px">First Name</div>
<div class="abs field" style="left:866px;top:2975px;width:183px">Last Name</div>
<div class="abs field" style="left:665px;top:3047px;width:182px">Email Address</div>
<div class="abs field" style="left:866px;top:3047px;width:183px">Phone Number</div>
<div class="abs field" style="left:665px;top:3119px;width:384px">Select Subject</div>
<div class="abs field" style="left:665px;top:3192px;width:384px">dd/mm/yyyy</div>
<div class="abs submit">SUBMIT</div>

<!-- reviews -->
<div class="abs reviews"></div>
<div class="abs section-title serif" style="top:3452px">Clients Review</div>
<div class="abs section-sub" style="top:3519px">Lorem ipsum dolor sit amet, consectetur adipiscing elit, sed do eiusmod temp<br>or incididunt ut labore et dolore</div>

<div class="abs review-card" style="left:102px"><div class="stars">★★★★★</div><p>Lorem ipsum dolor sit amet, consectetur adipiscing elit, sed do eiusmod or incididun t ut labore et dolore Lorem ipsum dolor sit adipiscing elit, sed do ehjhj</p><h5>Nora Whitfield</h5><small>BUSINESSMAN</small></div>
<div class="abs review-card active" style="left:444px"><div class="stars">★★★★★</div><p>Lorem ipsum dolor sit amet, consectetur adipiscing elit, sed do eiusmod or incididun t ut labore et dolore Lorem ipsum dolor sit adipiscing elit, sed do ehjhj</p><h5>Nora Whitfield</h5><small>BUSINESSMAN</small></div>
<div class="abs review-card" style="left:786px"><div class="stars">★★★★★</div><p>Lorem ipsum dolor sit amet, consectetur adipiscing elit, sed do eiusmod or incididun t ut labore et dolore Lorem ipsum dolor sit adipiscing elit, sed do ehjhj</p><h5>Nora Whitfield</h5><small>BUSINESSMAN</small></div>
<div class="abs avatar" style="left:133px" role="img" aria-label="Client portrait"></div>
<div class="abs avatar" style="left:475px" role="img" aria-label="Client portrait"></div>
<div class="abs avatar" style="left:817px;background:linear-gradient(135deg,#9aa3ad,#3c4450)" role="img" aria-label="Client portrait"></div>
<div class="abs quote-mark" style="left:328px">”</div>
<div class="abs quote-mark" style="left:670px">”</div>
<div class="abs quote-mark" style="left:1012px">”</div>

<!-- footer -->
<div class="abs footer"></div>
<svg class="abs" style="left:0;top:3946px" width="1200" height="160" viewBox="0 0 1200 160">
  <path d="M0,0 L1200,0 Q600,186 0,0Z" fill="#f1eff6"/>
  <path d="M245,88 Q600,150 955,88" fill="none" stroke="#2d9cf5" stroke-width="4"/>
  <circle cx="603" cy="123" r="28" fill="#fff"/>
</svg>
<div class="abs footer-brand">Calloway Pool Service</div>
<div class="abs footer-link" style="left:356px">HOME</div>
<div class="abs footer-link" style="left:458px">SERVICES</div>
<div class="abs footer-link" style="left:568px">ABOUT US</div>
<div class="abs footer-link" style="left:702px">TESTIMONIALS</div>
<div class="abs footer-link" style="left:821px">BLOG</div>
<div class="abs footer-rule"></div>
<div class="abs footer-divider" style="left:430px"></div>
<div class="abs footer-divider" style="left:751px"></div>
<div class="abs footer-contact" style="left:180px">
  <div class="ring"><svg width="26" height="26" viewBox="0 0 24 24"><circle cx="12" cy="12" r="9" fill="none" stroke="#fff" stroke-width="1.3"/><path d="M3 12h18M12 3c3 3 3 15 0 18M12 3c-3 3-3 15 0 18" fill="none" stroke="#fff" stroke-width="1.3"/></svg></div>
  <div>123, Building Name, Street<br>City, State XY 123456</div>
</div>
<div class="abs footer-contact" style="left:510px">
  <div class="ring"><svg width="22" height="26" viewBox="0 0 20 24"><rect x="4" y="2" width="12" height="20" rx="2" fill="none" stroke="#fff" stroke-width="1.3"/><path d="M9 19h2" stroke="#fff" stroke-width="1.3"/></svg></div>
  <div>PHONE<br>(123) 456 7890</div>
</div>
<div class="abs footer-contact" style="left:833px">
  <div class="ring"><svg width="26" height="26" viewBox="0 0 24 24"><path d="M3 9l9-6 9 6v11H3z M3 9l9 6 9-6" fill="none" stroke="#fff" stroke-width="1.3"/></svg></div>
  <div>EMAIL<br>info@company.com</div>
</div>
<div class="abs bottom-bar"><span>Calloway Pool Service</span></div>
<div class="abs social" style="left:933px"></div>
<div class="abs social" style="left:966px"></div>
<div class="abs social" style="left:999px"></div>
<div class="abs social" style="left:1032px"></div>

</body>
</html>
```